Website for 9 year old artist, helps animal rescue charity :)

I am looking to have a simple website created for my 9 year old son's small "company." He makes necklaces and art out of beachcombed treasures and sells them for animal rescue charity. Currently, his domain name www.gullcovepebblecraft.com brings people straight to his chatterly page, but for those who are not on CH, nothing shows up.

I would like a simple landing page + a few other clickable pages that will show his logo (already done by Pixel Guild folks!) +
* photos
* a brief description about what he does
* a link to the charities he supports
* link to his Chatterly Page (https://www.chatterly.com/GullCovePebblecraft)
* are where a link to a possible wovly store could go (future, we haven't gotten that far). :)
(really just a "shop" button)
I need to be able to add and remove photos and text, add calendar dates of events he will be at, and adjust links if needed.

I hope this isn't too complicated! It doesn't need to be flashy, just an easy on the eyes page where people who are interested in his necklaces and his charity work can go to find out more. I would like to have the website incorporate the two logos (see uploads). I image the image of the child beachcombing being on the bottom anchoring the page, but that is as far as my imagination has gone regarding the web design! :)

UPDATED:
Name of web url: www.gullcovepebblecraft.com
Name of company: Gull Cove Pebblecraft
Purpose: Owen is 9 years old. He beachcombs with his family all over the United States and finds wonderful shells, seaglass, and pottery. His mom helps him drill the holes in these piece and then he creates one of a kind necklaces using these beachcombed treasures and silver charms. He also makes sweet shell, seaglass and driftwood angels (Owen's Seraphs). All shells are responsibly collected. Every piece is designed by Owen.

At least 20% off all proceeds from every sale goes to animal rescue charity.

Target Market(s)

The target market for his necklaces is typically women, but we have a lot of guys buy them, too, to hang in their windows or to give away. All ages of folks buy his necklaces at the small sales and fairs we have gone to. They also look at his site to find out more about Willow Lane Feline Shelter, the organization Owen donates a lot of his proceeds to.

We get a lot of requests about whether he has a webpage and find that many of the people who want to check it out do not have Chatterly, so linking right to CH hasn't worked.

Industry/Entity Type

Charity

Requirements
Must have
• * Logos (I have 2 done by design works folks). The one of the beachcombing child is for the website only, the one of the shell angel will be for the website and business cards, etc.
* Spaces for photos
* Clickable links to Chatterly, Wovly (later), charity(s) he donates to
* Space for Bio/backstory
* Contact us area

Match the blues of the two logos so they are the same shade.

The look should be young and simple, without being childish. We are beachcombers at heart, so sea and sand colors would work great. All blues (except electric), greens, tans, etc are great.

I added a ton of images for reference. Please message me if you would like more.
Nice to have
• * Area I can add the tally of how much he has donated so far
* Slideshow of images (I uploaded a ton for examples)
* Page dedicated to images and information about the of the rescue organization he primarily donates to. The rescue organization is dedicated to the rehabilitation and adoption of special needs and abused cats.
Should not have
• Curlz font or anything too cutesy

Bright colors, I am hoping for a more muted, seas-inspired look.

```html
<!DOCTYPE html>
<html lang="en">
<head>
<meta charset="utf-8">
<title>Gull Cove Pebblecraft – Charity Store</title>
<link href="https://fonts.googleapis.com/css2?family=Bree+Serif&family=Open+Sans:wght@400;600;700&display=swap" rel="stylesheet">
<style>
  :root {
    --topbar: #2a2a2a;
    --nav: #333333;
    --sand: #dcd8cc;
    --page: #e3e3e3;
    --white: #ffffff;
    --aqua: #1bbfcc;
    --ink: #111111;
    --body-text: #666666;
    --muted: #9a9a9a;
    --countdown: #1c1c1c;
    --line: #f5f5f5;
  }
  * { box-sizing: border-box; margin: 0; padding: 0; }
  html, body { width: 1200px; height: 680px; overflow: hidden; }
  body {
    position: relative;
    font-family: "Open Sans", Arial, sans-serif;
    background: var(--page);
    background-image: repeating-linear-gradient(45deg, rgba(255,255,255,0.25) 0 2px, transparent 2px 5px);
    color: var(--ink);
  }

  /* top contact bar */
  .topbar { position: absolute; left: 0; top: 0; width: 1200px; height: 52px; background: var(--topbar); border-top: 2px solid #4a4a4a; }
  .contact { position: absolute; left: 166px; top: 15px; color: #bdbdbd; font-size: 8.5px; line-height: 14px; }
  .contact span { display: inline-flex; align-items: center; gap: 3px; margin-right: 9px; }
  .contact svg { fill: #bdbdbd; }
  .social { position: absolute; left: 724px; top: 20px; display: flex; gap: 16px; }
  .social i { display: block; width: 7px; height: 7px; border-radius: 50%; background: #e6e6e6; }
  .cart { position: absolute; left: 914px; top: 0; width: 83px; height: 58px; background: var(--white); color: var(--aqua); font-size: 9px; font-weight: 700; }
  .cart-label { position: absolute; left: 22px; top: 16px; display: flex; align-items: center; gap: 7px; color: #8a8a8a; font-weight: 600; }
  .cart-label svg { fill: var(--aqua); }
  .cart-count { position: absolute; left: 22px; top: 40px; }

  /* brand band */
  .brand-band { position: absolute; left: 0; top: 52px; width: 1200px; height: 118px; background: var(--sand); }
  .brand-art { position: absolute; left: 176px; top: 5px; width: 160px; height: 106px; background: linear-gradient(180deg, #c9d7d6 0%, #9fd3d8 100%); border-bottom: 4px solid var(--aqua); }
  .brand-name { position: absolute; left: 272px; top: 30px; font-family: "Bree Serif", Georgia, serif; font-size: 22px; color: var(--aqua); }
  .event { position: absolute; left: 593px; top: 34px; width: 405px; height: 43px; background: var(--countdown); display: flex; }
  .event-title { width: 183px; display: flex; align-items: center; justify-content: center; font-family: "Bree Serif", Georgia, serif; font-size: 17px; color: var(--aqua);
    background-image: repeating-linear-gradient(45deg, rgba(255,255,255,0.06) 0 1px, transparent 1px 3px); }
  .unit { border-left: 1px solid #3c3c3c; color: var(--white); text-align: center; padding-top: 8px; font-size: 11px; line-height: 11px; }
  .unit b { display: block; font-size: 16px; line-height: 15px; font-weight: 700; }
  .unit.days { width: 45px; } .unit.hours { width: 43px; } .unit.minutes { width: 55px; } .unit.seconds { width: 55px; }
  .event-more { width: 24px; background: var(--aqua); color: var(--white); display: flex; align-items: center; justify-content: center; font-size: 14px; }

  /* navigation */
  .nav { position: absolute; left: 0; top: 170px; width: 1200px; height: 43px; background: var(--nav); }
  .nav ul { position: absolute; left: 177px; top: 15px; display: flex; gap: 20px; list-style: none; }
  .nav li { color: var(--white); font-size: 9px; font-weight: 600; letter-spacing: -0.1px; }
  .search { position: absolute; left: 851px; top: 10px; width: 147px; height: 26px; background: #262626; }
  .search svg { position: absolute; right: 5px; top: 9px; }

  .breadcrumb { position: absolute; left: 192px; top: 220px; font-size: 9px; color: #555; }
  .breadcrumb a { color: var(--aqua); text-decoration: none; }

  /* products header */
  .products-head { position: absolute; left: 182px; top: 252px; width: 803px; height: 55px; background: var(--white); }
  .products-head h1 { position: absolute; left: 0; top: 15px; height: 26px; border-left: 3px solid var(--aqua); padding-left: 8px; font-size: 19px; font-weight: 600; line-height: 26px; color: #222; }
  .filters { position: absolute; left: 312px; top: 13px; display: flex; gap: 7px; }
  .filters span { border: 1px solid #cfcfcf; background: #f7f7f7; font-size: 9.5px; color: #555; padding: 3px 7px 4px; }
  .divider { position: absolute; left: 182px; top: 324px; width: 803px; height: 2px; background: var(--line); }

  /* product grid */
  .grid { position: absolute; left: 184px; top: 340px; display: grid; grid-template-columns: repeat(4, 185px); column-gap: 17px; row-gap: 15px; }
  .card { position: relative; width: 185px; height: 289px; background: var(--white); }
  .card-photo { position: absolute; left: 6px; top: 11px; width: 173px; height: 108px; }
  .photo-ribbon { background: linear-gradient(120deg, #7a3e14 0%, #a8774a 45%, #2f47a8 60%, #8a5a2e 100%); }
  .photo-table { background: linear-gradient(135deg, #b9a488 0%, #8b7c6c 45%, #c4b8aa 100%); }
  .card h2 { position: absolute; left: 7px; top: 134px; font-size: 15px; font-weight: 700; color: var(--ink); }
  .card p { position: absolute; left: 7px; top: 160px; width: 172px; font-size: 9.5px; line-height: 13.5px; color: var(--body-text); }
  .price { position: absolute; left: 7px; top: 218px; color: var(--aqua); font-size: 18px; }
  .price sup { font-size: 11px; vertical-align: 6px; }
  .price s { color: var(--muted); font-size: 11px; }
  .price s sup { font-size: 8px; vertical-align: 3px; }
  .add-btn { position: absolute; right: 7px; top: 253px; width: 79px; height: 22px; background: var(--aqua); color: var(--white); border-radius: 2px; font-size: 9.5px; font-weight: 600; display: flex; align-items: center; justify-content: center; }
  .next-row .card-photo { height: 108px; }
  .photo-grey { background: linear-gradient(180deg, #9b9b9b, #d6d6d6); }
  .photo-kraft { background: linear-gradient(180deg, #e9ddc4, #c8ad83); }
  .photo-mug { background: linear-gradient(180deg, #f2f2f2, #dcdcdc); }
  .photo-tee { background: linear-gradient(180deg, #c7c7c7, #efefef); }
</style>
</head>
<body>

<header class="topbar">
  <div class="contact">
    <span><svg width="6" height="8" viewBox="0 0 6 8"><path d="M3 0a3 3 0 0 0-3 3c0 2 3 5 3 5s3-3 3-5a3 3 0 0 0-3-3zm0 4a1 1 0 1 1 0-2 1 1 0 0 1 0 2z"/></svg>12 Harbor Lane, Portland, USA</span><br>
    <span><svg width="6" height="8" viewBox="0 0 6 8"><rect x="0.5" y="0" width="5" height="8" rx="1"/></svg>+00 42 615 78 20</span>
    <span><svg width="8" height="6" viewBox="0 0 8 6"><path d="M0 0h8v6H0z M0 0l4 3 4-3" stroke="#2a2a2a" stroke-width="0.7"/></svg>hello@gullcovepebblecraft.com</span>
  </div>
  <div class="social" aria-label="Social links">
    <i></i><i></i><i></i><i></i><i></i><i></i>
  </div>
  <div class="cart">
    <div class="cart-label"><svg width="12" height="10" viewBox="0 0 12 10"><path d="M0 0h2l1.8 6h6.2L12 1.5H3.2" /><circle cx="4.5" cy="8.8" r="1.1"/><circle cx="9" cy="8.8" r="1.1"/></svg>Cart</div>
    <div class="cart-count">2 &nbsp;items</div>
  </div>
</header>

<section class="brand-band">
  <div class="brand-art" role="img" aria-label="Illustration of a child beachcombing along the shoreline"></div>
  <div class="brand-name">Gull Cove Pebblecraft</div>
  <div class="event">
    <div class="event-title">Upcoming Event</div>
    <div class="unit days"><b>465</b>Days</div>
    <div class="unit hours"><b>9</b>Hours</div>
    <div class="unit minutes"><b>0</b>Minutes</div>
    <div class="unit seconds"><b>56</b>Seconds</div>
    <div class="event-more">+</div>
  </div>
</section>

<nav class="nav">
  <ul>
    <li>HOME</li><li>ABOUT</li><li>BLOG</li><li>CHARITY EVENTS</li><li>CHARITY STORE</li><li>GALLERY</li><li>FEATURES</li><li>CROWDFUNDING</li><li>CONTACT</li>
  </ul>
  <div class="search"><svg width="8" height="8" viewBox="0 0 8 8"><circle cx="3.2" cy="3.2" r="2.4" fill="none" stroke="#ddd" stroke-width="1.2"/><path d="M5 5l2.5 2.5" stroke="#ddd" stroke-width="1.4"/></svg></div>
</nav>

<div class="breadcrumb"><a href="#">Home</a> / Charity Store</div>

<section class="products-head">
  <h1>Products</h1>
  <div class="filters"><span>All</span><span>Shopping</span></div>
</section>
<div class="divider"></div>

<main class="grid">
  <article class="card">
    <div class="card-photo photo-ribbon" role="img" aria-label="Shell angels on driftwood beside a blue prize ribbon"></div>
    <h2>Be Human Cup</h2>
    <p>Nunc faucibus congue sem, ut fringilla sem. Maecenas sed porttitor nibh, at ornare justo. Aliquam sit amet leo commodo, fringilla tortor a, vehicula r</p>
    <div class="price"><sup>£</sup>55<s><sup>£</sup>22</s></div>
    <div class="add-btn">Add to cart</div>
  </article>
  <article class="card">
    <div class="card-photo photo-table" role="img" aria-label="Worktable covered with beachcombed shells and craft supplies"></div>
    <h2>Support Our Cause</h2>
    <p>Nunc faucibus congue sem, ut fringilla sem. Maecenas sed porttitor nibh, at ornare justo. Aliquam sit amet leo commodo, fringilla tortor a, vehicula r</p>
    <div class="price"><sup>£</sup>55<s><sup>£</sup>22</s></div>
    <div class="add-btn">Add to cart</div>
  </article>
  <article class="card">
    <div class="card-photo photo-ribbon" role="img" aria-label="Shell angels on driftwood beside a blue prize ribbon"></div>
    <h2>Be Human Cup</h2>
    <p>Nunc faucibus congue sem, ut fringilla sem. Maecenas sed porttitor nibh, at ornare justo. Aliquam sit amet leo commodo, fringilla tortor a, vehicula r</p>
    <div class="price"><sup>£</sup>55<s><sup>£</sup>22</s></div>
    <div class="add-btn">Add to cart</div>
  </article>
  <article class="card">
    <div class="card-photo photo-table" role="img" aria-label="Worktable covered with beachcombed shells and craft supplies"></div>
    <h2>Give Hope Cap</h2>
    <p>Nunc faucibus congue sem, ut fringilla sem. Maecenas sed porttitor nibh, at ornare justo. Aliquam sit amet leo commodo, fringilla tortor a, vehicula r</p>
    <div class="price"><sup>£</sup>55<s><sup>£</sup>22</s></div>
    <div class="add-btn">Add to cart</div>
  </article>
  <article class="card next-row"><div class="card-photo photo-grey" role="img" aria-label="Grey printed shirt product photo"></div></article>
  <article class="card next-row"><div class="card-photo photo-kraft" role="img" aria-label="Kraft paper gift box product photo"></div></article>
  <article class="card next-row"><div class="card-photo photo-mug" role="img" aria-label="White mug product photo"></div></article>
  <article class="card next-row"><div class="card-photo photo-tee" role="img" aria-label="White t-shirt product photo"></div></article>
</main>

</body>
</html>
```